Design clean technology service-based company website

Hello, We are looking to reskin our company website. We are an environmental inspection company and test for Asbestos, Lead and Mold along with other contaminants. People depend on the results to be accurate and fast. We are regulated by the EPA and State regulations. We work a lot with business to business and business to customer. We are wanting to make our new presentation to be modern and easy for customers to interact with us, understand our process and services while providing valuable environmental informational resource and updates. We are a technology based company and will be providing instantaneous results as reports come in for the customers. We are needing good calls to action on the site to direct them to setup a new inspection. Each user will have a backend access to their job information with invoices, reports, status, etc. We have developed software to be able to proved these reports and want to look the part.

My current website is www.trypelmarix.com

Helllo we are wanting to make sure we have good time to select the right website for us and also have the additional time to select other pages of the website. We have received great designs and have consolidated our requests into a document for the next set of iterations.

Target Market(s)

Home Owners, Contractors, Engineers, Real Estate Agents, Building Owners, Insurance Adjusters

Industry/Entity Type

Environmental Consultant

Number of Pages Required

5+ page

Font styles to use
Sans Serif

Colors
0355a3
9bcb3c
7f7f7f
f5f5f5
000000

Requirements
Must have
• Use our existing logo to design around
• The layouts look good in mobile mode for understanding and selecting services and signing up
• Clean Modern Layout
• Have all pages on the website have a similar layout and feel
• Clearly communicate services along with bundle service packages
• Detail the customer journey with graphic design
• Great call to actions to either schedule inspection online, call, text, chat
Nice to have
• Have an interactive graphic for where to test for lead, asbestos and mold.
• I like the barney kolts top order line bar - see attached
• Have clear question and answer page layouts for asbestos, lead and mold
• Show Company reviews
• Have clear Resources pages for all types of contaminants
Should not have
• My current website is www.trypelmarix.com

```html
<!DOCTYPE html>
<html lang="en">
<head>
<meta charset="utf-8">
<title>Pelmarix – Environmental Inspections</title>
<link rel="stylesheet" href="https://fonts.googleapis.com/css2?family=Montserrat:wght@500;600;700&family=Nunito+Sans:wght@400;600;700&display=swap">
<style>
:root{
  --blue:#0355a3;
  --blue-dark:#024a8f;
  --green:#5cc21a;
  --green-soft:#9bcb3c;
  --grey:#7f7f7f;
  --grey-dark:#636466;
  --light:#f5f5f5;
  --black:#000;
  --ink:#333;
  --dark:#222;
  --white:#fff;
}
*{box-sizing:border-box;margin:0;padding:0}
html,body{width:1200px;height:2908px;overflow:hidden}
body{position:relative;font-family:"Nunito Sans",Arial,sans-serif;color:var(--ink);background:var(--white)}
.abs{position:absolute}
.heading{font-family:"Montserrat",Arial,sans-serif;font-weight:600;letter-spacing:2px;text-transform:uppercase}
.btn{position:absolute;display:flex;align-items:center;justify-content:center;white-space:nowrap;background:var(--green);color:var(--white);font-family:"Montserrat",Arial,sans-serif;font-weight:700;font-size:17px;letter-spacing:1.5px;text-transform:uppercase;border-bottom:3px solid #3f9a0d}

/* header */
.site-header{position:absolute;left:0;top:0;width:1200px;height:140px;background:linear-gradient(#d6e9f9,#c3dcf2)}
.brand{left:85px;top:20px;font-family:"Montserrat",Arial,sans-serif;font-weight:700;font-size:56px;color:var(--green);letter-spacing:1px}
.badge-plain{position:absolute;background:var(--blue-dark);border-radius:3px}
.response{left:938px;top:22px;font-size:15px;color:var(--ink);font-weight:600}
.contact-line{top:58px;font-size:15px;color:var(--ink);display:flex;align-items:center;gap:8px}
.social{display:flex;gap:6px}
.social span{width:24px;height:24px;border-radius:50%;background:var(--blue)}
.main-nav{position:absolute;left:0;top:102px;width:1200px;height:38px;border-top:1px solid #a9c7e3;display:flex;justify-content:space-between;padding:0 87px;align-items:center}
.main-nav a{font-family:"Montserrat",Arial,sans-serif;font-size:15px;letter-spacing:2px;color:var(--grey-dark);text-decoration:none;text-transform:uppercase}
.main-nav a.active{color:var(--blue);font-weight:700}

/* hero */
.hero{position:absolute;left:0;top:140px;width:1200px;height:433px;background:linear-gradient(180deg,#8fa5b8 0%,#6f7478 40%,#4e4f4f 100%)}
.hero-title{left:0;top:118px;width:1200px;text-align:center;color:var(--white);font-family:"Montserrat",Arial,sans-serif;font-weight:700;font-size:46px;line-height:48px;letter-spacing:2px;text-transform:uppercase;white-space:nowrap}
.hero-strip{left:50%;top:216px;transform:translateX(-50%);padding:0 10px;height:30px;background:var(--blue);color:var(--white);white-space:nowrap;font-family:"Montserrat",Arial,sans-serif;font-size:17px;letter-spacing:2.5px;line-height:30px}

/* cta band */
.cta-band{position:absolute;left:0;top:573px;width:1200px;height:120px;background:var(--blue);color:var(--white)}
.cta-band h2{position:absolute;left:85px;top:22px;font-size:28px;letter-spacing:2px}
.cta-band p{position:absolute;left:85px;top:60px;width:820px;font-size:16px;line-height:24px}

/* about */
.about{position:absolute;left:0;top:693px;width:1200px;height:377px;background:radial-gradient(ellipse at 60% 40%,#eeeae0,#d8d2c2)}
.photo{position:absolute;background:linear-gradient(135deg,#e9eef2,#b9c6cf)}
.about h2{position:absolute;left:658px;top:86px;color:var(--blue);font-size:27px;line-height:30px;letter-spacing:2px}
.about p{position:absolute;left:658px;top:150px;width:320px;font-size:13px;line-height:20px;color:var(--grey-dark)}

/* services */
.services{position:absolute;left:0;top:1070px;width:1200px;height:634px;background:#262626}
.services h2{position:absolute;left:85px;top:54px;color:var(--white);font-size:30px}
.card{position:absolute;border:1px solid #4a4a4a;background:#1f1f1f}
.card h3{position:absolute;font-family:"Montserrat",Arial,sans-serif;font-weight:600;font-size:16px;color:var(--green);text-transform:uppercase;letter-spacing:.5px}
.card p{position:absolute;font-size:13.5px;line-height:21px;color:#e6e6e6}
.card u{color:#e6e6e6}

/* why */
.why{position:absolute;left:0;top:1704px;width:1200px;height:459px;background:linear-gradient(#f7f7f7,#e2e2e2)}
.why h2{position:absolute;left:85px;top:56px;color:var(--blue);font-size:27px}
.reason{position:absolute;left:85px;width:700px}
.reason .num{position:absolute;left:0;top:0;width:46px;height:46px;border-radius:50%;background:var(--green);color:var(--white);font-family:"Montserrat",Arial,sans-serif;font-size:22px;font-weight:600;display:flex;align-items:center;justify-content:center}
.reason h3{position:absolute;left:66px;top:0;font-family:"Montserrat",Arial,sans-serif;font-weight:700;font-size:16px;letter-spacing:.5px;color:var(--black);text-transform:uppercase;white-space:nowrap}
.reason p{position:absolute;left:66px;top:24px;width:640px;font-size:13px;line-height:21px;color:var(--grey-dark)}

/* partners */
.partners{position:absolute;left:0;top:2163px;width:1200px;height:249px;background:var(--white)}
.partner{position:absolute;top:64px;width:325px;height:123px;border:1px solid #ddd;background:var(--white)}
.arrow{position:absolute;top:110px;width:24px;height:26px;background:#555;display:flex;align-items:center;justify-content:center;z-index:2}

/* footer */
.footer-left{position:absolute;left:0;top:2412px;width:600px;height:459px;background:var(--grey-dark);color:var(--white)}
.footer-right{position:absolute;left:600px;top:2412px;width:600px;height:459px;background:var(--green);color:var(--white)}
.footer-left h2,.footer-right h2{position:absolute;top:36px;font-size:22px;letter-spacing:2px}
.f-label{position:absolute;font-family:"Montserrat",Arial,sans-serif;font-weight:700;font-size:15px;letter-spacing:1px;text-transform:uppercase}
.f-text{position:absolute;font-size:13px;line-height:20px}
.quick-links{position:absolute;left:321px;top:78px;list-style:none;font-size:13px;line-height:21px}
.footer-brand{left:0;top:2752px;width:1200px;text-align:center;font-family:"Montserrat",Arial,sans-serif;font-weight:700;font-size:56px;line-height:70px;color:var(--white);z-index:3}
.copyright{position:absolute;left:0;top:2871px;width:1200px;height:37px;background:var(--blue);color:var(--white);text-align:center;font-size:13px;line-height:37px;letter-spacing:1px}
</style>
</head>
<body>

<header class="site-header">
  <div class="abs brand">Pelmarix</div>
  <div class="badge-plain" style="left:835px;top:17px;width:88px;height:34px"></div>
  <div class="abs response">24/7 Same Day Response</div>
  <div class="abs contact-line" style="left:602px">
    <svg width="26" height="26" viewBox="0 0 26 26"><circle cx="13" cy="13" r="12" fill="none" stroke="#5cc21a" stroke-width="2"/><path d="M9 7l3 3-2 2c1 2 3 4 5 5l2-2 3 3-2 2c-5 0-11-6-11-11z" fill="#5cc21a"/></svg>
    <span>303 555 0142</span>
  </div>
  <div class="abs contact-line" style="left:752px">
    <svg width="26" height="20" viewBox="0 0 26 20"><rect x="1" y="1" width="24" height="18" fill="none" stroke="#5cc21a" stroke-width="2"/><path d="M1 1l12 10L25 1" fill="none" stroke="#5cc21a" stroke-width="2"/></svg>
    <span>info@trypelmarix.com</span>
  </div>
  <div class="abs social" style="left:968px;top:59px"><span></span><span></span><span></span><span></span><span></span></div>
  <nav class="main-nav">
    <a class="active" href="#">Home</a><a href="#">Our Services</a><a href="#">Resources</a><a href="#">Blog</a><a href="#">Q&amp;A</a><a href="#">Reviews</a><a href="#">Connect</a>
  </nav>
</header>

<section class="hero" role="img" aria-label="Close view of a weathered corrugated asbestos cement roof under a pale sky">
  <h1 class="abs hero-title">Fast, Dependable Results<br>When It Matters The Most</h1>
  <div class="abs hero-strip">PROUDLY SERVING &nbsp;-&nbsp; DENVER &nbsp;|&nbsp; COLORADO SPRINGS &nbsp;|&nbsp; BOULDER</div>
  <a class="btn" style="left:479px;top:263px;width:242px;height:38px">Schedule Inspection</a>
</section>

<section class="cta-band">
  <h2 class="heading">New Construction Project?</h2>
  <p>Let us start you in the right direction with our certified asbestos inspections …Residential, commercial, schools, governmental properties, multi-family and more.</p>
  <a class="btn" style="left:970px;top:42px;width:143px;height:38px">Call Now</a>
</section>

<section class="about">
  <div class="photo" style="left:219px;top:64px;width:412px;height:248px;box-shadow:0 3px 10px rgba(0,0,0,.3)" role="img" aria-label="Laboratory scientist in safety glasses and blue gloves holding a petri dish"></div>
  <h2 class="heading">Environmental<br>Testing Evolved</h2>
  <p>Pelmarix grew up in the rough and tumble disaster restoration industry. Time and time again, we saw projects small and large brought to a stand-still to await environmental testing and results.</p>
  <a class="btn" style="left:658px;top:247px;width:143px;height:38px">Read More</a>
</section>

<section class="services">
  <h2 class="heading">Our Services</h2>
  <article class="card" style="left:85px;top:106px;width:501px;height:221px">
    <div class="photo" style="left:0;top:0;width:238px;height:219px;background:linear-gradient(160deg,#9cc3e6 0%,#8a8d8a 45%,#5d5e5a 100%)" role="img" aria-label="Worn asbestos shingle roof with a chimney"></div>
    <h3 style="left:264px;top:24px">Asbestos Inspections</h3>
    <p style="left:264px;top:52px;width:220px">There are many variations of passages of Lorem Ipsum available, but the majority have suffered alteration in some form, by injected humour, or randomised words which don't look even slightly believable...<u>READ MORE</u></p>
  </article>
  <article class="card" style="left:613px;top:106px;width:501px;height:221px">
    <div class="photo" style="left:0;top:0;width:238px;height:219px;background:radial-gradient(circle,#d9dccb,#8f9674)" role="img" aria-label="Magnified mold spores"></div>
    <h3 style="left:264px;top:24px">Mold Inspections</h3>
    <p style="left:264px;top:52px;width:220px">There are many variations of passages of Lorem Ipsum available, but the majority have suffered alteration in some form, by injected humour, or randomised words which don't look even slightly believable...<u>READ MORE</u></p>
  </article>
  <article class="card" style="left:85px;top:352px;width:1029px;height:220px">
    <div class="photo" style="left:0;top:0;width:419px;height:218px;background:linear-gradient(170deg,#7fb0e0 0%,#dfe3e6 40%,#b9bdc0 100%)" role="img" aria-label="Old white clapboard house with peeling paint under repair"></div>
    <h3 style="left:557px;top:22px">Lead Based Paint Testing</h3>
    <p style="left:557px;top:48px;width:452px">There are many variations of passages of Lorem Ipsum available, but the majority have suffered alteration in some form, by injected humour, or randomised words which don't look even slightly believable. All the Lorem Ipsum generators on the Internet tend to repeat predefined chunks as necessary, making this the first true generator on the Internet. It uses a dictionary of over 200 Latin words, combined with a handful of model sentence structures, to generate Lorem Ipsum which looks reasonable...<u>READ MORE</u></p>
  </article>
</section>

<section class="why">
  <h2 class="heading">Why Choose Us</h2>
  <div class="reason" style="top:100px"><span class="num">1</span><h3>We're Serious About Our Work</h3><p>We'll show up at your door with a smile and treat you like a new friend. But be assured that we're all business when it comes to delivering professional testing and consulting services.</p></div>
  <div class="reason" style="top:190px"><span class="num">2</span><h3>Fast, Accurate Test Results. Very Fast.</h3><p>For any environmental testing to be meaningful, much less valuable, you need the results to be reliable and fast. If it takes until mold spores become visible over a large area to get positive mold contamination test results, those results aren't really "news." They're "olds."</p></div>
  <div class="reason" style="top:304px"><span class="num">3</span><h3>We Treat Your Family and Business Like Ours</h3><p>We never forget that our business is about people. Protecting people from hazards. When we enter your home or business, we consider how we would want to protect our home or business.</p></div>
  <div class="photo" style="left:830px;top:20px;width:290px;height:439px;background:linear-gradient(180deg,#e9e9e9,#cfd3d8)" role="img" aria-label="Inspector in a white hard hat and tie holding rolled plans"></div>
</section>

<section class="partners">
  <div class="arrow" style="left:85px"><svg width="10" height="12" viewBox="0 0 10 12"><path d="M8 0L1 6l7 6z" fill="#fff"/></svg></div>
  <div class="partner" style="left:85px"><div class="badge-plain" style="left:57px;top:22px;width:210px;height:79px"></div></div>
  <div class="partner" style="left:438px"><div class="abs" style="left:30px;top:14px;width:96px;height:96px;border-radius:50%;background:#5cc21a"></div><div class="abs" style="left:140px;top:36px;width:150px;height:52px;background:#333"></div></div>
  <div class="partner" style="left:790px"><div class="abs" style="left:28px;top:34px;width:80px;height:56px;background:#2aa06a"></div><div class="abs" style="left:124px;top:30px;width:172px;height:64px;background:#4a5a6a"></div></div>
  <div class="arrow" style="left:1090px"><svg width="10" height="12" viewBox="0 0 10 12"><path d="M2 0l7 6-7 6z" fill="#fff"/></svg></div>
</section>

<footer>
  <div class="footer-left">
    <h2 class="heading" style="left:87px">Customer Journey</h2>
    <div class="f-text" style="left:89px;top:74px;font-weight:700;font-size:15px">2015-06-23</div>
    <div class="f-text" style="left:89px;top:94px;color:#5cc21a;font-size:18px;letter-spacing:3px">★★★★★</div>
    <p class="f-text" style="left:85px;top:124px;width:380px">We needed an asbestos test done before we could have our floors replaced. Dale and his staff were pleasant and prompt. We had the testing completed and the...</p>
    <div class="f-label" style="left:85px;top:196px;font-size:13px">By Home Owner</div>
    <a class="btn" style="left:87px;top:230px;width:143px;height:38px;border:2px solid #fff;font-size:15px;letter-spacing:1px">View Review</a>
    <p class="f-text" style="left:248px;top:230px;width:250px;font-size:15px">Authentic. Positive. Reviews | Powered by <span style="color:#5cc21a">ReviewLoopMedia</span></p>
    <div class="badge-plain" style="left:89px;top:294px;width:142px;height:56px"></div>
    <div class="f-text" style="left:248px;top:312px;font-weight:700;font-size:12px">Click for Profile</div>
  </div>
  <div class="footer-right">
    <h2 class="heading" style="left:44px">Contact Info</h2>
    <div class="f-label" style="left:44px;top:78px">Address</div>
    <p class="f-text" style="left:44px;top:102px;width:240px">4120 E. Meadow Ave. Ste. 210 Denver, Co. 80222</p>
    <div class="f-label" style="left:44px;top:150px">Phone</div>
    <p class="f-text" style="left:44px;top:174px">303-555-0142</p>
    <div class="f-label" style="left:44px;top:202px">Email</div>
    <p class="f-text" style="left:44px;top:226px">info@trypelmarix.com</p>
    <div class="f-label" style="left:44px;top:256px">Social Links</div>
    <div class="abs social" style="left:44px;top:284px"><span></span><span></span><span></span><span></span><span></span></div>
    <h2 class="heading" style="left:321px">Quick Links</h2>
    <ul class="quick-links"><li>Home</li><li>Our Services</li><li>Resources</li><li>Blog</li><li>Q &amp; A</li><li>Reviews</li><li>Connect</li></ul>
  </div>
  <div class="abs footer-brand">Pelmarix</div>
  <div class="copyright">© 2017 &nbsp;|&nbsp; All Rights Reserved.</div>
</footer>

</body>
</html>
```